Request for Business Card Design

Hi. My name is Marlena, I am looking for a new business card design for my company, Quillbrook Sensing Systems, LLC. I really like the design you did for Tavel Harvest and was hoping you could do something similar using our full logo and our mark. I am also open to any raised texture design using our mark. I have attached our full logo, which would need to be somewhere on the card, as well as the mark in both outline and full form, as well as our brand colors / guide. The card does not have to be white, as long as our logo and mark appear. I actually like darker colored business cards more, but am open to all options. If you are interested in working with me, please let me know. We would also take the business card design into letterhead design if you can do that.

```html
<!DOCTYPE html>
<html lang="en">
<head>
<meta charset="utf-8">
<title>Quillbrook Sensing Systems — Business Card</title>
<link rel="stylesheet" href="https://fonts.googleapis.com/css2?family=Open+Sans:wght@400;600;700&display=swap">
<style>
  :root {
    --backdrop: #212121;
    --card-dark: #3b3b3d;
    --card-blue: #1898c4;
    --card-blue-deep: #0f86b0;
    --card-blue-light: #6cc3e0;
    --accent: #1b95c2;
    --ink-light: #ffffff;
    --ink-soft: #e6e6e6;
  }
  * { box-sizing: border-box; margin: 0; padding: 0; }
  html, body {
    width: 1200px;
    height: 780px;
    overflow: hidden;
    background: var(--backdrop);
    font-family: "Open Sans", Arial, sans-serif;
  }
  .card-pair {
    position: absolute;
    inset: 0;
    display: flex;
    align-items: center;
    justify-content: center;
    gap: 40px;
  }
  .card {
    position: relative;
    width: 530px;
    height: 304px;
    border-radius: 2px;
    overflow: hidden;
    box-shadow: 0 12px 30px rgba(0,0,0,0.45);
  }

  /* Front */
  .card-front { background: var(--card-dark); color: var(--ink-light); }
  .contact {
    position: absolute;
    left: 28px;
    top: 28px;
    font-size: 12.5px;
    line-height: 1.45;
    color: var(--ink-soft);
  }
  .contact-address { margin-bottom: 8px; }
  .contact-list { list-style: none; }
  .contact-list li { display: flex; align-items: center; gap: 8px; }
  .contact-icon { width: 11px; height: 11px; fill: var(--accent); flex: none; }

  .brand {
    position: absolute;
    display: flex;
    align-items: center;
    gap: 12px;
  }
  .brand-dot { border-radius: 50%; flex: none; }
  .brand-name {
    font-weight: 700;
    text-transform: uppercase;
    line-height: 1.1;
  }
  .card-front .brand { right: 28px; top: 34px; }
  .card-front .brand-dot { width: 40px; height: 40px; background: var(--accent); }
  .card-front .brand-name { font-size: 19px; letter-spacing: 2px; color: var(--ink-light); }

  .holder {
    position: absolute;
    right: 34px;
    bottom: 30px;
    text-align: right;
  }
  .holder-name { font-size: 34px; font-weight: 600; color: var(--accent); line-height: 1.1; }
  .holder-role { font-size: 15px; color: var(--ink-light); }

  /* Back */
  .card-back { background: var(--card-blue); }
  .mark-texture {
    position: absolute;
    inset: 0;
    background: linear-gradient(100deg, var(--card-blue-deep) 0%, var(--card-blue) 55%, var(--card-blue-light) 100%);
  }
  .card-back .brand { left: 30px; bottom: 26px; }
  .card-back .brand-dot { width: 18px; height: 18px; background: var(--ink-light); }
  .card-back .brand-name { font-size: 11px; letter-spacing: 1px; color: var(--ink-light); }
</style>
</head>
<body>
<main class="card-pair">

  <section class="card card-front" aria-label="Business card front">
    <div class="contact">
      <p class="contact-address">1180 Fenwick Park Road •<br>Ashcombe, CO 80611</p>
      <ul class="contact-list">
        <li>
          <svg class="contact-icon" viewBox="0 0 24 24" aria-hidden="true"><path d="M6.6 10.8a15.1 15.1 0 0 0 6.6 6.6l2.2-2.2c.3-.3.7-.4 1-.2 1.1.4 2.3.6 3.6.6.6 0 1 .4 1 1V20c0 .6-.4 1-1 1A17 17 0 0 1 3 4c0-.6.4-1 1-1h3.5c.6 0 1 .4 1 1 0 1.3.2 2.5.6 3.6.1.3 0 .7-.2 1z"/></svg>
          +001 555 210 4482
        </li>
        <li>
          <svg class="contact-icon" viewBox="0 0 24 24" aria-hidden="true"><path d="M6 2h12v6H6zM3 9h18v9h-3v4H6v-4H3zm5 7v4h8v-4z"/></svg>
          +001 555 210 4490
        </li>
        <li>
          <svg class="contact-icon" viewBox="0 0 24 24" aria-hidden="true"><path d="M12 2a10 10 0 1 0 0 20 10 10 0 0 0 0-20zm6.9 9h-3a15 15 0 0 0-1.3-5.6A8 8 0 0 1 18.9 11zM12 4c.9 1.2 1.7 3.6 1.9 7h-3.8c.2-3.4 1-5.8 1.9-7zM9.4 5.4A15 15 0 0 0 8.1 11h-3a8 8 0 0 1 4.3-5.6zM5.1 13h3a15 15 0 0 0 1.3 5.6A8 8 0 0 1 5.1 13zm6.9 7c-.9-1.2-1.7-3.6-1.9-7h3.8c-.2 3.4-1 5.8-1.9 7zm2.6-1.4a15 15 0 0 0 1.3-5.6h3a8 8 0 0 1-4.3 5.6z"/></svg>
          www.quillbrooksensing.com
        </li>
        <li>
          <svg class="contact-icon" viewBox="0 0 24 24" aria-hidden="true"><path d="M2 5h20v14H2zm2 2v.5l8 5 8-5V7zm0 2.8V17h16V9.8l-8 5z"/></svg>
          hello@quillbrooksensing.com
        </li>
      </ul>
    </div>

    <div class="brand">
      <span class="brand-dot" aria-hidden="true"></span>
      <p class="brand-name">Quillbrook<br>Sensing Systems</p>
    </div>

    <div class="holder">
      <p class="holder-name">Marlena</p>
      <p class="holder-role">Director</p>
    </div>
  </section>

  <section class="card card-back" aria-label="Business card back">
    <div class="mark-texture" role="img" aria-label="Repeating pattern of the company mark in deep blue, fading to light blue and white toward the right edge"></div>
    <div class="brand">
      <span class="brand-dot" aria-hidden="true"></span>
      <p class="brand-name">Quillbrook<br>Sensing Systems</p>
    </div>
  </section>

</main>
</body>
</html>
```